Coralbend Pastoral Traders Business Cards

We require business cards revamped with our logo. A few details we would like to use.

1. Round Edges
2. Our logo over the top of a wagyu cattle background photo on one side of the card

Other side of the card has the below details.

1. Person Name (First & Last)
2. Job Position
3. Mobile Number
4. Email Address
5. Website Address

Simple & Neat.

Target Market(s)

Sales

Industry/Entity Type

Agriculture

Contact Information for Business Card

CORALBEND PASTORAL TRADERS

Colors

Designer to choose colors to be used in the design.

Requirements
Must have
• Company Logo

```html
<!DOCTYPE html>
<html lang="en">
<head>
<meta charset="utf-8">
<title>Coralbend Pastoral Traders Business Cards</title>
<link href="https://fonts.googleapis.com/css2?family=Open+Sans:wght@400;600;700&display=swap" rel="stylesheet">
<style>
  :root {
    --maroon: #6a1820;
    --ink: #060608;
    --hide: #1c1c1f;
    --white: #ffffff;
    --page: #fefefe;
  }
  * { margin: 0; padding: 0; box-sizing: border-box; }
  html, body { width: 1200px; height: 860px; overflow: hidden; background: var(--page); }
  body { position: relative; font-family: 'Open Sans', Arial, sans-serif; color: var(--white); }

  .card {
    position: absolute;
    top: 286px;
    width: 444px;
    height: 287px;
    border-radius: 48px;
    overflow: hidden;
  }
  .card--front { left: 131px; background: var(--ink); }
  .card--back { left: 625px; background: var(--ink); }

  .card__shapes { position: absolute; inset: 0; width: 100%; height: 100%; }

  .cattle-photo {
    position: absolute;
    inset: 0;
    background:
      radial-gradient(ellipse 60% 45% at 55% 48%, #2a2a2e 0%, rgba(20,20,22,0.6) 55%, rgba(6,6,8,0) 100%),
      radial-gradient(ellipse 18% 30% at 95% 30%, #25252a 0%, rgba(6,6,8,0) 100%),
      linear-gradient(180deg, var(--ink) 0%, var(--ink) 18%, var(--hide) 45%, #141416 100%);
  }

  .brand {
    position: absolute;
    text-align: center;
    font-weight: 600;
    color: var(--white);
    line-height: 1;
  }
  .brand__name { display: block; letter-spacing: 0.02em; }
  .brand__tagline {
    display: flex;
    align-items: center;
    justify-content: center;
    gap: 6px;
    letter-spacing: 0.28em;
  }
  .brand__tagline::before, .brand__tagline::after {
    content: "";
    display: block;
    height: 1px;
    background: var(--white);
    flex: 1;
  }

  .card--front .brand { left: 72px; top: 116px; width: 300px; }
  .card--front .brand__name { font-size: 40px; }
  .card--front .brand__tagline { font-size: 10px; margin-top: 6px; }

  .card--back .brand { left: 104px; top: 38px; width: 240px; }
  .card--back .brand__name { font-size: 32px; }
  .card--back .brand__tagline { font-size: 8px; margin-top: 5px; }

  .person { position: absolute; left: 29px; top: 194px; }
  .person__name { font-size: 18.5px; font-weight: 700; letter-spacing: 0.01em; line-height: 1.1; }
  .person__role { font-size: 14.5px; font-weight: 400; margin-top: 3px; line-height: 1.1; }

  .contacts { position: absolute; left: 236px; top: 194px; list-style: none; }
  .contacts__item {
    display: flex;
    align-items: center;
    gap: 7px;
    font-size: 11px;
    height: 17px;
    letter-spacing: 0.01em;
  }
  .contacts__icon { width: 14px; height: 14px; flex: none; }
</style>
</head>
<body>

  <section class="card card--front">
    <div class="cattle-photo" role="img" aria-label="Photo of a black wagyu cow standing in profile against a dark background"></div>
    <svg class="card__shapes" viewBox="0 0 444 287" aria-hidden="true">
      <path d="M0,193 C110,196 230,236 300,236 C365,236 415,208 444,188 L444,287 L0,287 Z" fill="var(--maroon)"/>
      <path d="M0,210 C100,208 220,250 300,250 C365,250 415,220 444,196" fill="none" stroke="var(--ink)" stroke-width="3.5"/>
    </svg>
    <div class="brand">
      <span class="brand__name">CORALBEND</span>
      <span class="brand__tagline">PASTORAL TRADERS</span>
    </div>
  </section>

  <section class="card card--back">
    <svg class="card__shapes" viewBox="0 0 444 287" aria-hidden="true">
      <path d="M0,0 L444,0 L444,116 C400,140 340,150 275,148 C200,144 110,105 42,105 C20,105 8,110 0,114 Z" fill="var(--maroon)"/>
      <path d="M0,139 C20,130 35,126 55,126 C120,126 220,162 327,162 C380,162 420,142 444,124" fill="none" stroke="var(--white)" stroke-width="4"/>
    </svg>
    <div class="brand">
      <span class="brand__name">CORALBEND</span>
      <span class="brand__tagline">PASTORAL TRADERS</span>
    </div>

    <div class="person">
      <p class="person__name">PERSON NAME</p>
      <p class="person__role">Job Position</p>
    </div>

    <ul class="contacts">
      <li class="contacts__item">
        <svg class="contacts__icon" viewBox="0 0 14 14" aria-hidden="true">
          <circle cx="7" cy="7" r="7" fill="var(--white)"/>
          <rect x="4.6" y="2.8" width="4.8" height="8.4" rx="0.9" fill="var(--ink)"/>
          <rect x="5.4" y="3.8" width="3.2" height="5.6" fill="var(--white)"/>
        </svg>
        <span>+00 123 456 789</span>
      </li>
      <li class="contacts__item">
        <svg class="contacts__icon" viewBox="0 0 14 14" aria-hidden="true">
          <circle cx="7" cy="7" r="7" fill="var(--white)"/>
          <rect x="3.4" y="4.5" width="7.2" height="5" rx="0.6" fill="none" stroke="var(--ink)" stroke-width="1"/>
          <path d="M3.6,4.8 L7,7.4 L10.4,4.8" fill="none" stroke="var(--ink)" stroke-width="1"/>
        </svg>
        <span>person@coralbendpastoral.com</span>
      </li>
      <li class="contacts__item">
        <svg class="contacts__icon" viewBox="0 0 14 14" aria-hidden="true">
          <circle cx="7" cy="7" r="7" fill="var(--white)"/>
          <circle cx="7" cy="7" r="3.8" fill="none" stroke="var(--ink)" stroke-width="0.9"/>
          <ellipse cx="7" cy="7" rx="1.6" ry="3.8" fill="none" stroke="var(--ink)" stroke-width="0.8"/>
          <path d="M3.2,7 H10.8" stroke="var(--ink)" stroke-width="0.8"/>
        </svg>
        <span>www.coralbendpastoral.com</span>
      </li>
    </ul>
  </section>

</body>
</html>
```